Halmi Rékas Physiotherapy Business Card Vienna

We need a business card design for a newly created Physiotherapy company based in Vienna Austria.
We seek a simple, modern, minimalist design without too much color variation. The font should look young/fresh, but definitely not childish or so. Since we are a starting Business, we currently haven't got a logo, if you feel like a logo would fit your design, feel free to use one, but it's not necessary.
Target Market(s)
Healthcare, young and elderly people with mobility issues
Industry/Entity Type
Health And Wellness
Contact Information for Business Card
Name: Réka Halmi
Title description: Physiotherapist
Phone num: +43 664 5290 4116
e-mail: reka.praxis@examplemail.net
Colors
Designer to choose colors to be used in the design.
Requirements
Must have
- Final design language must be in German, basically, the Title Description needs to be "Physiotherapeutin" the other details remain as in the English Language.
Nice to have
- Simple, modern, minimalist design
Should not have
- too many colors, Obvious use of a skeleton, skull, spline

```html
<!DOCTYPE html>
<html lang="de">
<head>
<meta charset="utf-8">
<title>Réka Halmi – Physiotherapeutin – Visitenkarte</title>
<link href="https://fonts.googleapis.com/css2?family=Montserrat:wght@300;400;600&display=swap" rel="stylesheet">
<style>
  :root {
    --page: #ecebe8;
    --ink: #161618;
    --paper: #f3f3f3;
    --white: #ffffff;
    --muted: #5a5a5c;
    --rule: #8a8a8a;
  }
  * { box-sizing: border-box; margin: 0; padding: 0; }
  html, body { width: 1200px; height: 1200px; overflow: hidden; }
  body {
    background: var(--page);
    font-family: "Montserrat", sans-serif;
    position: relative;
  }
  .card {
    position: absolute;
    width: 706px;
    height: 402px;
    box-shadow: 0 2px 6px rgba(0,0,0,0.18);
    overflow: hidden;
  }

  /* Front */
  .card-front { left: 247px; top: 103px; background: var(--ink); color: var(--white); }
  .card-front .corner { position: absolute; left: 0; top: 0; width: 706px; height: 402px; }
  .front-brand {
    position: absolute; left: 0; right: 0; top: 86px;
    text-align: center;
    font-weight: 400; font-size: 22px; letter-spacing: 0.04em;
    color: var(--muted);
  }
  .front-name {
    position: absolute; left: 0; right: 0; top: 188px;
    text-align: center;
    font-weight: 600; font-size: 46px; letter-spacing: 0.02em;
    font-variant: small-caps; line-height: 1;
  }
  .front-title {
    position: absolute; left: 0; right: 0; top: 243px;
    text-align: center;
    font-weight: 300; font-size: 26px; letter-spacing: 0.03em;
    font-variant: small-caps; line-height: 1;
  }

  /* Back */
  .card-back { left: 250px; top: 627px; background: var(--ink); }
  .back-panel {
    position: absolute; left: 10px; top: 12px; right: 10px; bottom: 12px;
    background: var(--paper); border-radius: 8px;
    box-shadow: inset 0 0 4px rgba(0,0,0,0.35);
    color: var(--ink);
    overflow: hidden;
  }
  .back-name {
    position: absolute; left: 33px; top: 84px;
    font-weight: 600; font-size: 38px; letter-spacing: 0.02em;
    font-variant: small-caps; line-height: 1;
  }
  .back-title {
    position: absolute; left: 33px; top: 124px;
    font-weight: 300; font-size: 25px; letter-spacing: 0.02em;
    font-variant: small-caps; line-height: 1;
  }
  .back-rule {
    position: absolute; left: 32px; top: 174px; width: 232px; height: 1px;
    background: var(--rule);
  }
  .contact {
    position: absolute; left: 43px; top: 203px;
    list-style: none; font-size: 18.5px; font-weight: 400; line-height: 32px;
  }
  .back-brand {
    position: absolute; left: 345px; top: 70px; width: 320px; height: 210px;
    display: flex; flex-direction: column; justify-content: center;
    font-weight: 600; font-size: 36px; line-height: 1.15;
    font-variant: small-caps; letter-spacing: 0.01em;
    white-space: nowrap;
  }
</style>
</head>
<body>
  <section class="card card-front" aria-label="Vorderseite">
    <svg class="corner" viewBox="0 0 706 402" aria-hidden="true">
      <polygon points="0,286 0,402 120,402" fill="#3a3a3a"/>
      <polygon points="0,289 0,402 117,402" fill="var(--white)"/>
    </svg>
    <p class="front-brand">Halmi Rékas Physiotherapy</p>
    <h1 class="front-name">Réka Halmi</h1>
    <p class="front-title">Physiotherapeutin</p>
  </section>

  <section class="card card-back" aria-label="Rückseite">
    <div class="back-panel">
      <h2 class="back-name">Réka Halmi</h2>
      <p class="back-title">Physiotherapeutin</p>
      <div class="back-rule"></div>
      <ul class="contact">
        <li class="contact-phone">+43 664 5290 4116</li>
        <li class="contact-email">reka.praxis@examplemail.net</li>
      </ul>
      <p class="back-brand"><span>Halmi</span><span>Rékas</span><span>Physiotherapy</span></p>
    </div>
  </section>
</body>
</html>
```